Sumworks.co.uk - front page and content page design
Site design for Sumworks.co.uk - a UK site hosting different calculators
Creative Brief
Internet Services
http://www.plotmeadow.co.uk
Project: Sumworks.co.uk
Idea: To host all of the different types of calculators on the site with supporting content
Our idea is generating targeted traffic through generic domains (we've got 4,500!). With Sumworks.co.uk, the domain will host loads of different calculators with content supporting the calculators on offer.
For Sumworks.co.uk, we'd like a design that is clean but colourful and allows us to colour the different sections of the site that we'll have. The initial premise is that we'll have sections for the different 'types' of calculators:
Health calculators
Finance calculators
Maths calculators
Conversion calculators
Pregnancy calculators
Within each section will be different calculators - so, for example, in Health, there will be a BMI calculator, BMR calculator and so on.
Ideally, we'd like each 'section' to have a different colour - i.e. blue for Health, green for Finance, blue for Maths, etc. The colours can be chosen by the designer as to what looks best.
We'd like a front page design and also a content page design. The home page shouldn't be too different in structure/layout to the content pages (i.e. structure follows through).
Ideally, there will be a column on the right hand side that allows advertising (300 x 250) and the main column for content should be at least 540px (this is where content and weidgets/calculators will be placed).
Once in a section, there should be a left menu that allows users to choose the type of calculator they want within that section.
This is our first try on Pixelgrove and we're hoping that if this works out, we can find some designer(s) through this who we can offer many more design projects as we have many generic domain names waiting to be designed.
Likes: Clean, colourful, elegant, professional
www.vitalpage.com
http://www.brightjotapp.com/tour/why-use-brightjot
http://www.kelvo.com/

```html
<!DOCTYPE html>
<html lang="en">
<head>
<meta charset="utf-8">
<title>Sumworks.co.uk — Calculators</title>
<link href="https://fonts.googleapis.com/css2?family=Open+Sans:wght@400;600;700;800&family=Nunito:wght@700;800&display=swap" rel="stylesheet">
<style>
:root{
  --ink:#333333;
  --muted:#8a8a8a;
  --rule:#d6d6d6;
  --teal:#1f8fa6;
  --health:#3aa3b8;
  --finance:#b8c46a;
  --maths:#e3c24a;
  --conversion:#ee8a3a;
  --pregnancy:#7cc3dc;
  --orange:#e9892f;
  --hero-bg:#ececea;
  --page:#ffffff;
}
*{margin:0;padding:0;box-sizing:border-box}
html,body{width:1200px;height:957px;overflow:hidden;background:var(--page)}
body{font-family:"Open Sans",Arial,sans-serif;color:var(--ink);position:relative}
.abs{position:absolute}

/* header */
.brand{left:182px;top:38px;font-weight:800;font-size:25px;letter-spacing:1px;color:#222}
.topline{left:151px;top:78px;width:905px;height:1px;background:var(--rule)}
.nav{left:409px;top:31px;display:flex;height:47px}
.nav a{display:flex;align-items:center;justify-content:center;color:#fff;text-decoration:none;font-size:12px;font-weight:600;letter-spacing:.5px}
.nav .home{width:68px;background:#fff;color:#444;border:1px solid var(--rule);border-bottom:none}
.nav .health{width:78px;background:var(--health)}
.nav .finance{width:86px;background:var(--finance)}
.nav .maths{width:84px;background:var(--maths)}
.nav .conversion{width:115px;background:var(--conversion)}
.nav .pregnancy{width:106px;background:var(--pregnancy)}

/* hero */
.hero{left:151px;top:96px;width:618px;height:477px;background:var(--hero-bg);overflow:hidden}
.hero-photo{position:absolute;right:0;top:0;width:330px;height:477px;background:linear-gradient(160deg,#f2f2f0 0%,#d9d6d0 45%,#7d7a76 70%,#e8e6e2 100%)}
.hero h1{position:absolute;left:31px;top:22px;width:340px;font-size:29px;line-height:35px;font-weight:700;color:var(--teal)}
.steps{position:absolute;left:31px;top:112px;display:flex;gap:42px}
.step{display:flex;flex-direction:column}
.step .num{display:flex;align-items:center;gap:6px;font-size:44px;font-weight:700;color:var(--teal);line-height:46px}
.step .label{font-size:10px;font-weight:700;color:var(--teal);margin-top:6px}
.hero p{position:absolute;left:31px;top:212px;width:240px;font-size:10px;line-height:15px;color:#666}
.hero .more{display:inline-block;background:#fff;border:1px solid #ccc;font-size:9px;padding:0 6px;margin-left:4px}

/* adverts */
.ad-travel{left:777px;top:96px;width:279px;height:235px;background:#3b3b38}
.ad-travel .head{padding:10px 14px;color:#fff}
.ad-travel .name{font-weight:700;font-size:20px;color:#fff}
.ad-travel .tag{font-size:14px;line-height:18px;color:#cfe69a;margin-top:6px}
.ad-travel .photo{position:absolute;left:0;top:118px;width:279px;height:117px;background:linear-gradient(90deg,#6d8a5a 0%,#8aa3b8 50%,#e9892f 75%,#2c2c2a 100%)}
.ad-trim{left:777px;top:339px;width:279px;height:234px;background:#fff;border:1px solid #e3e3e3;overflow:hidden}
.ad-trim .photo{position:absolute;right:0;top:0;width:132px;height:234px;background:linear-gradient(180deg,#f1dccb 0%,#d9a98a 60%,#e8e4e0 100%)}
.ad-trim .name{position:absolute;left:12px;top:10px;font-weight:800;font-size:24px;color:#333;line-height:26px}
.ad-trim .name small{display:block;font-size:10px;letter-spacing:2px;font-weight:600;line-height:14px}
.ad-trim .lose{position:absolute;left:12px;top:60px;font-weight:800;color:var(--orange);line-height:1}
.ad-trim .lose .big{display:block;font-size:50px;line-height:52px}
.ad-trim .lose .row{display:flex;align-items:center;gap:4px}
.ad-trim .lose .sm{font-size:12px}
.ad-trim .lose .n{font-size:72px;line-height:76px}
.ad-trim .lose .p{display:block;font-size:28px;line-height:32px}

/* lower columns */
.col{top:630px;width:292px;height:254px}
.col h2{font-family:"Nunito",sans-serif;font-weight:800;font-size:27px;color:#3a3a3a;text-align:center;margin-top:2px}
.col p{font-size:10px;line-height:14px;color:#777;text-align:center;margin:8px auto 0;width:250px}
.col .rule{position:absolute;left:0;top:112px}
.col .art{position:absolute;left:116px;top:136px;width:60px;height:58px;background:linear-gradient(180deg,#d9a86a,#6b87b5)}
.col-social{left:151px}
.col-suggest{left:458px}
.col-news{left:763px}
.topbar{position:absolute;left:0;top:0;width:292px;height:1px;background:var(--rule)}
.icons{display:flex;gap:4px;justify-content:center;margin-top:10px}
.icons span{width:13px;height:13px;background:var(--health)}
.icons span:nth-child(3n){background:var(--orange)}
.icons span:nth-child(4n){background:#999}
.cta{position:absolute;left:112px;top:200px;background:#fff;border:1px solid #aaa;font-size:9px;padding:1px 6px}
.email{position:absolute;left:40px;top:216px;width:210px;height:28px;border:1px solid #bbb;font-size:10px;color:#888;padding:7px 8px;background:#fff}
.email svg{position:absolute;right:8px;top:8px}

/* footer */
.foot{left:151px;top:895px;width:905px;height:28px;border-top:1px solid var(--rule);border-bottom:1px solid var(--rule);display:flex;align-items:center;justify-content:space-between;padding:0 10px;font-size:9px;color:#777}
.foot .brand-sm{font-weight:800;font-size:13px;color:#555;letter-spacing:1px}
</style>
</head>
<body>
<div class="abs brand">SUMWORKS</div>
<nav class="abs nav">
  <a class="home" href="#">HOME</a>
  <a class="health" href="#">HEALTH</a>
  <a class="finance" href="#">FINANCE</a>
  <a class="maths" href="#">MATHS</a>
  <a class="conversion" href="#">CONVERSION</a>
  <a class="pregnancy" href="#">PREGNANCY</a>
</nav>
<div class="abs topline"></div>

<section class="abs hero">
  <div class="hero-photo" role="img" aria-label="Photo of a woman sitting on the floor with a laptop"></div>
  <h1>Get calculators results with 3 easy steps</h1>
  <div class="steps">
    <div class="step">
      <div class="num">1<svg width="26" height="28" viewBox="0 0 26 28"><rect x="1" y="1" width="24" height="26" fill="none" stroke="#e9892f" stroke-width="2"/><path d="M9 8l9 7-4 1 2 5-2 1-2-5-3 3z" fill="#e9892f"/></svg></div>
      <div class="label">SELECT A CATEGORY</div>
    </div>
    <div class="step">
      <div class="num">2<svg width="26" height="28" viewBox="0 0 26 28"><rect x="1" y="1" width="24" height="26" fill="none" stroke="#e9892f" stroke-width="2"/><path d="M13 6v12M8 13l5 5 5-5M7 22h12" fill="none" stroke="#e9892f" stroke-width="2"/></svg></div>
      <div class="label">FILL THE FIELDS</div>
    </div>
    <div class="step">
      <div class="num">3<svg width="26" height="28" viewBox="0 0 26 28"><rect x="1" y="1" width="24" height="26" fill="none" stroke="#e9892f" stroke-width="2"/><path d="M7 9h12M7 14h12M7 19h12" stroke="#e9892f" stroke-width="2"/></svg></div>
      <div class="label">GET RESULTS</div>
    </div>
  </div>
  <p>Lorem ipsum dolor sit amet, consectetur adipiscing elit. In malesuada elementum ante, et ultricies elit aliquet vitae. Sed pharetra sapien. Praesent molestie. <span class="more">more</span></p>
</section>

<aside class="abs ad-travel">
  <div class="head">
    <div class="name">Waypoint Breaks</div>
    <div class="tag">Planning advice and video travel guides for your next trip away!</div>
  </div>
  <div class="photo" role="img" aria-label="Travel photos of a mountain landscape and a map"></div>
</aside>
<aside class="abs ad-trim">
  <div class="photo" role="img" aria-label="Photo of a slim waist with a tape measure"></div>
  <div class="name">Leanleaf<small>NUTRITION</small></div>
  <div class="lose"><span class="big">LOSE</span><span class="row"><span class="sm">up to</span><span class="n">20</span></span><span class="p">POUNDS</span></div>
</aside>

<section class="abs col col-social">
  <div class="topbar"></div>
  <h2>we are sociable</h2>
  <p>Share us with the world the way you want!</p>
  <div class="icons"><span></span><span></span><span></span><span></span><span></span><span></span><span></span><span></span><span></span><span></span><span></span><span></span></div>
  <svg class="rule" width="292" height="12"><path d="M0 1H138l8 9 8-9H292" fill="none" stroke="#d6d6d6"/></svg>
  <div class="art" role="img" aria-label="Illustration of two people sitting on a bench"></div>
</section>
<section class="abs col col-suggest">
  <div class="topbar"></div>
  <h2>suggestions</h2>
  <p>Didn't you find what you are looking for? or you simply has a suggestion to help us improve? Let us know and we will take care of it right away!</p>
  <svg class="rule" width="292" height="12"><path d="M0 1H138l8 9 8-9H292" fill="none" stroke="#d6d6d6"/></svg>
  <div class="art" role="img" aria-label="Illustration of a person at a desk"></div>
  <span class="cta">contact form</span>
</section>
<section class="abs col col-news">
  <div class="topbar"></div>
  <h2>newsletter</h2>
  <p>Register your email address if you would like to know when new calculators are available and make 'CRAZY' offers and discounts from our partners!</p>
  <svg class="rule" width="292" height="12"><path d="M0 1H138l8 9 8-9H292" fill="none" stroke="#d6d6d6"/></svg>
  <div class="art" role="img" aria-label="Illustration of a person holding an envelope"></div>
  <div class="email">Enter email<svg width="8" height="12" viewBox="0 0 8 12"><path d="M1 1l5 5-5 5" fill="none" stroke="#777" stroke-width="1.5"/></svg></div>
</section>

<footer class="abs foot">
  <span class="brand-sm">SUMWORKS</span>
  <span>FAQ | About Sumworks | Privacy policy</span>
  <span>© 2011 sumworks.co.uk. All rights reserved</span>
</footer>
</body>
</html>
```